Health care technology software systems

We have a solid logo. We have company colors that will need to be used as well. We just need a great business card design. We sell to health plans but want to be modern
Updates

Need extra days to review

Target Market(s)

Health technology sector selling into Health Plans

Industry/Entity Type

Health Care Technology

Contact Information for Business Card

Name, title, address, phone number, email

Requirements
Must have
• Use of Kembrata corporate colors - Uploaded w/ our logos

```html
<!DOCTYPE html>
<html lang="en">
<head>
<meta charset="utf-8">
<title>Kembrata Business Cards</title>
<link href="https://fonts.googleapis.com/css2?family=Roboto:wght@300;400;500;700&display=swap" rel="stylesheet">
<style>
  :root {
    --stage: #6a6a6a;
    --paper: #ffffff;
    --ink: #3a3a3a;
    --ink-soft: #555555;
    --navy: #2e4a9a;
    --sky: #29a8e0;
    --leaf: #7dc242;
  }
  * { box-sizing: border-box; margin: 0; padding: 0; }
  html, body { width: 1200px; height: 876px; overflow: hidden; }
  body {
    background: var(--stage);
    font-family: "Roboto", Arial, sans-serif;
    color: var(--ink);
    position: relative;
  }
  .card {
    position: absolute;
    width: 540px;
    height: 309px;
    background: var(--paper);
    top: 284px;
    box-shadow: 0 6px 18px rgba(0,0,0,0.25);
  }
  .card--contact { left: 45px; }
  .card--brand { left: 615px; }

  .wordmark {
    position: absolute;
    display: flex;
    align-items: center;
    font-weight: 300;
    color: var(--ink);
    line-height: 1;
  }
  .wordmark__dot {
    border-radius: 50%;
    background: var(--sky);
    flex: none;
  }
  .card--contact .wordmark { left: 40px; top: 42px; font-size: 40px; gap: 12px; }
  .card--contact .wordmark__dot { width: 26px; height: 26px; }
  .card--brand .wordmark { left: 112px; top: 92px; font-size: 64px; gap: 18px; }
  .card--brand .wordmark__dot { width: 42px; height: 42px; }

  .web-line {
    position: absolute;
    left: 112px;
    top: 196px;
    font-size: 10px;
    letter-spacing: 6px;
    color: var(--ink);
  }
  .accent-bar {
    position: absolute;
    left: 60px;
    top: 218px;
    width: 420px;
    height: 7px;
    display: flex;
    border-radius: 4px;
    overflow: hidden;
  }
  .accent-bar__navy { width: 50px; background: var(--navy); }
  .accent-bar__sky { flex: 1; background: var(--sky); }
  .accent-bar__leaf { width: 60px; background: var(--leaf); }

  .person {
    position: absolute;
    left: 238px;
    top: 100px;
    display: flex;
    gap: 12px;
  }
  .person__icon { width: 26px; height: 28px; margin-top: 2px; }
  .person__name { font-size: 22px; font-weight: 500; color: var(--ink); }
  .person__title { font-size: 11px; color: var(--ink-soft); margin-top: 2px; }
  .person__rule { width: 42px; height: 2px; background: var(--leaf); margin-top: 6px; }

  .contact-pill {
    position: absolute;
    left: 240px;
    top: 166px;
    width: 26px;
    height: 78px;
    background: var(--leaf);
    border-radius: 6px;
  }
  .contact-list {
    position: absolute;
    left: 280px;
    top: 170px;
    list-style: none;
    font-size: 14px;
    color: var(--ink);
  }
  .contact-list li { height: 25px; }
  .address {
    position: absolute;
    left: 240px;
    top: 254px;
    font-size: 14px;
    font-style: normal;
    line-height: 20px;
    color: var(--ink-soft);
  }
</style>
</head>
<body>

<section class="card card--contact">
  <div class="wordmark"><span class="wordmark__dot"></span>kembrata</div>

  <div class="person">
    <svg class="person__icon" viewBox="0 0 26 28" aria-hidden="true">
      <circle cx="13" cy="7" r="6.5" fill="var(--sky)"/>
      <path d="M1 27 C1 18 6 15 13 15 C20 15 25 18 25 27 Z" fill="var(--sky)"/>
    </svg>
    <div>
      <div class="person__name">Daniel Reyes</div>
      <div class="person__title">Health Care Technology</div>
      <div class="person__rule"></div>
    </div>
  </div>

  <svg class="contact-pill" viewBox="0 0 26 78" aria-hidden="true">
    <path d="M9 9 l3 -2 l2 3 l-2 1.5 q1 2.5 3.5 3.5 l1.5 -2 l3 2 l-2 3 q-7 -1 -9 -9 z" fill="#fff"/>
    <rect x="8" y="33" width="10" height="8" rx="1" fill="#fff"/>
    <path d="M8 34 l5 4 l5 -4" stroke="var(--leaf)" stroke-width="1" fill="none"/>
    <circle cx="13" cy="62" r="5.5" fill="none" stroke="#fff" stroke-width="1.3"/>
    <path d="M7.5 62 h11 M13 56.5 q-3 5.5 0 11 q3 -5.5 0 -11" stroke="#fff" stroke-width="1" fill="none"/>
  </svg>
  <ul class="contact-list">
    <li>+000 123 456 7890</li>
    <li>yourgmail@name.com</li>
    <li>www.websitename.com</li>
  </ul>
  <address class="address">
    your street address place here<br>
    new yerk city, zip code - 000
  </address>
</section>

<section class="card card--brand">
  <div class="wordmark"><span class="wordmark__dot"></span>kembrata</div>
  <div class="web-line">www.websitename.com</div>
  <div class="accent-bar">
    <span class="accent-bar__navy"></span>
    <span class="accent-bar__sky"></span>
    <span class="accent-bar__leaf"></span>
  </div>
</section>

</body>
</html>
```